Larkspur Realty

Business cards for 4 people

They need to say for all
57 Danner Quay, Boston MA 02117

Each person will have their own personal information
We would like gold embossing for the name of the company
Mabel is the blonde sitting in the chair smiling her information should be on the back of the card with her name and information
Should say for slogan classic pattern, elevated experience
mabel@larkspurhomesnet.com
(413) 555-0182

Odessa is the brunette with wavy hair in the tan suit odessa@larkspurhomesnet.com
(617) 555-0147

june@larkspurhomesnet.com
(413) 555-0169
standing next to the chair

ruth@larkspurhomesnet.com
(413) 555-0193
close up headshot

```html
<!DOCTYPE html>
<html lang="en">
<head>
<meta charset="utf-8">
<title>Larkspur Realty – Business Card</title>
<link rel="stylesheet" href="https://fonts.googleapis.com/css2?family=Poppins:wght@400;500;700&family=Lato:wght@400&display=swap">
<style>
  :root {
    --backdrop: #a4ccc8;
    --paper: #fbfbfa;
    --navy: #1b2f55;
    --gold: #e8b551;
    --ink: #1f1f24;
    --portrait: #c4c4c4;
  }
  * { box-sizing: border-box; margin: 0; padding: 0; }
  html, body { width: 1200px; height: 1200px; overflow: hidden; }
  body { background: var(--backdrop); position: relative; }

  .card { position: absolute; width: 444px; height: 277px; overflow: hidden; }
  .card--front { left: 378px; top: 281px; background: var(--paper); }
  .card--back { left: 377px; top: 657px; background: var(--navy); }

  .accent-ring {
    position: absolute; left: 49px; top: 82px; width: 122px; height: 122px;
    border-radius: 50%; border: 5px solid var(--gold);
  }
  .accent-band {
    position: absolute; left: 0; top: 81px; width: 116px; height: 123px;
    background: var(--navy);
  }
  .portrait {
    position: absolute; left: 51px; top: 96px; width: 93px; height: 93px;
    border-radius: 50%;
    background: radial-gradient(circle at 50% 70%, #2a2a2e 0 30%, var(--portrait) 31%);
  }

  .identity { position: absolute; left: 202px; top: 71px; }
  .identity__name {
    font-family: 'Poppins', sans-serif; font-weight: 700; font-size: 26px;
    color: var(--navy); letter-spacing: 0.5px; line-height: 1;
  }
  .identity__role {
    font-family: 'Poppins', sans-serif; font-weight: 400; font-size: 11.5px;
    color: var(--ink); margin: 4px 0 0 3px; line-height: 1;
  }
  .identity__rule {
    width: 140px; height: 2px; background: var(--gold); margin: 8px 0 0 3px;
  }

  .contacts { position: absolute; left: 203px; top: 137px; list-style: none; }
  .contacts__item {
    display: flex; align-items: center; height: 20px; margin-bottom: 6px;
    font-family: 'Lato', sans-serif; font-size: 12px; color: var(--ink);
  }
  .contacts__icon { width: 20px; height: 20px; margin-right: 9px; flex: none; }

  .brand {
    position: absolute; left: 0; right: 0; top: 80px; text-align: center;
    font-family: 'Poppins', sans-serif; font-weight: 500; color: var(--gold);
  }
  .brand__mark {
    width: 68px; height: 68px; margin: 0 auto 16px; border-radius: 50%;
    border: 2px solid var(--gold);
  }
  .brand__name { font-size: 23px; letter-spacing: 1px; line-height: 1; }
  .brand__sub { font-size: 9px; letter-spacing: 10px; margin-top: 4px; padding-left: 10px; line-height: 1; }
</style>
</head>
<body>

<section class="card card--front">
  <div class="accent-ring"></div>
  <div class="accent-band"></div>
  <div class="portrait" role="img" aria-label="Portrait photo of Mabel seated in a chair, smiling"></div>

  <div class="identity">
    <h1 class="identity__name">MABEL</h1>
    <p class="identity__role">RECEPTION</p>
    <div class="identity__rule"></div>
  </div>

  <ul class="contacts">
    <li class="contacts__item">
      <svg class="contacts__icon" viewBox="0 0 20 20" aria-hidden="true">
        <circle cx="10" cy="10" r="10" fill="var(--navy)"/>
        <path d="M6.6 5.2c.4-.3.9-.2 1.1.2l1 1.8c.2.4.1.8-.2 1.1l-.7.6c.5 1.2 1.4 2.1 2.6 2.7l.6-.7c.3-.3.8-.4 1.1-.2l1.8 1c.4.2.5.7.2 1.1l-.8 1c-.4.5-1.1.6-1.7.4-3-1.1-5.1-3.3-6.1-6.2-.2-.6 0-1.3.4-1.7z" fill="#fff"/>
      </svg>
      (413) 555-0182
    </li>
    <li class="contacts__item">
      <svg class="contacts__icon" viewBox="0 0 20 20" aria-hidden="true">
        <circle cx="10" cy="10" r="10" fill="var(--navy)"/>
        <rect x="5" y="6.5" width="10" height="7" rx="1" fill="none" stroke="#fff" stroke-width="1.3"/>
        <path d="M5.3 7l4.7 3.6L14.7 7M5.3 13.2l3.4-3M14.7 13.2l-3.4-3" fill="none" stroke="#fff" stroke-width="1.1"/>
      </svg>
      mabel@larkspurhomesnet.com
    </li>
    <li class="contacts__item">
      <svg class="contacts__icon" viewBox="0 0 20 20" aria-hidden="true">
        <circle cx="10" cy="10" r="10" fill="var(--navy)"/>
        <path d="M10 4.5a4 4 0 0 1 4 4c0 3-4 7-4 7s-4-4-4-7a4 4 0 0 1 4-4z" fill="#fff"/>
        <circle cx="10" cy="8.5" r="1.5" fill="var(--navy)"/>
      </svg>
      57 Danner Quay, Boston MA 02117
    </li>
  </ul>
</section>

<section class="card card--back">
  <div class="brand">
    <div class="brand__mark"></div>
    <p class="brand__name">LARKSPUR</p>
    <p class="brand__sub">REALTY</p>
  </div>
</section>

</body>
</html>
```